KT Crewing business card

Require business card which includes:
Company name: KT CREWING PTY LTD
Email: Mick@ktcrewing.com.au
Phone: 0431 256 049
ACN: 718 235 946

slogan: Onsite Auto Electrician Labour hire

Details and logo on top side
Logo only on bottom side

colour codes : #F15A29 , #939598

Target Market(s)

Western Australia mining sector

Industry/Entity Type

Mining

Contact Information for Business Card

Require business card which includes: Company name: KT CREWING PTY LTD Email: Mick@ktcrewing.com.au Phone: 0431 256 049 ACN: 718 235 946 slogan: Onsite Auto Electrician Labour hire Details and logo on top side Logo only on bottom side colour codes : #F15A29 , #939598

Colors
EE7325
F08F49
F5BC92
FAE3D3
FDF4ED

Requirements
Must have
• double sided

```html
<!DOCTYPE html>
<html lang="en">
<head>
<meta charset="utf-8">
<title>KT Crewing Business Card</title>
<link href="https://fonts.googleapis.com/css2?family=Roboto:wght@400;700&display=swap" rel="stylesheet">
<style>
  :root {
    --stage: #2a2a2a;
    --brand-orange: #F15A29;
    --card-orange: #E0522A;
    --deep-orange: #B5401C;
    --brand-grey: #939598;
    --card-dark: #242424;
    --text-light: #b9babc;
    --white: #f4f4f4;
  }
  * { margin: 0; padding: 0; box-sizing: border-box; }
  html, body {
    width: 1200px; height: 1138px; overflow: hidden;
    background: var(--stage);
    font-family: 'Roboto', sans-serif;
  }
  .canvas { position: relative; width: 1200px; height: 1138px; }
  .card {
    position: absolute; width: 620px; height: 376px;
    border-radius: 16px; overflow: hidden;
  }
  .card--front {
    left: 272px; top: 184px;
    background: linear-gradient(180deg, #E25A2E 0%, var(--card-orange) 100%);
    display: flex; align-items: center; justify-content: center;
  }
  .front-wordmark {
    font-weight: 700; font-size: 56px; color: var(--deep-orange);
    letter-spacing: 1px; white-space: nowrap;
  }
  .card--back {
    left: 274px; top: 606px; height: 375px;
    background: linear-gradient(160deg, #2c2c2c 0%, var(--card-dark) 60%, #1f1f1f 100%);
  }
  .contact-list { position: absolute; left: 46px; top: 68px; list-style: none; }
  .contact-item {
    display: flex; align-items: center; height: 24px;
    font-size: 16px; color: var(--text-light);
  }
  .contact-icon { width: 16px; height: 16px; margin-right: 15px; fill: var(--brand-orange); }
  .company-details { position: absolute; left: 46px; top: 200px; color: var(--text-light); font-size: 16px; line-height: 24px; }
  .acn { margin-bottom: 6px; }
  .acn-label { color: var(--brand-orange); }
  .back-wordmark {
    position: absolute; left: 330px; top: 96px; width: 254px; text-align: right;
    font-weight: 700; font-size: 44px; color: var(--brand-orange); white-space: nowrap;
  }
  .footer-band {
    position: absolute; left: 0; right: 0; bottom: 0; height: 92px;
    background: linear-gradient(180deg,
      var(--brand-grey) 0, var(--brand-grey) 7px,
      #1c1c1c 7px, #1c1c1c 12px,
      var(--brand-orange) 12px, #D94C22 100%);
  }
  .person { position: absolute; right: 26px; top: 296px; text-align: right; color: var(--white); }
  .person-name { font-weight: 700; font-size: 24px; line-height: 28px; }
  .person-title { font-size: 17px; line-height: 22px; }
</style>
</head>
<body>
<main class="canvas">
  <section class="card card--front" aria-label="Card front">
    <div class="front-wordmark">KT Crewing</div>
  </section>

  <section class="card card--back" aria-label="Card back">
    <div class="footer-band" role="img" aria-label="Decorative footer band in grey and orange"></div>

    <ul class="contact-list">
      <li class="contact-item">
        <svg class="contact-icon" viewBox="0 0 16 16"><path d="M2 5c0-2 3-3 6-3s6 1 6 3v1h-3V5H5v1H2zM4 7h8l2 6H2z"/></svg>
        0431 256 049
      </li>
      <li class="contact-item">
        <svg class="contact-icon" viewBox="0 0 16 16"><path d="M1 3h14v10H1zM2 4l6 5 6-5v1L8 10 2 5z" fill-rule="evenodd"/></svg>
        Mick@ktcrewing.com.au
      </li>
      <li class="contact-item">
        <svg class="contact-icon" viewBox="0 0 16 16"><circle cx="8" cy="8" r="6.5"/><path d="M1.5 8h13M8 1.5v13M3 4.5h10M3 11.5h10" stroke="#242424" stroke-width="1" fill="none"/></svg>
        www.ktcrewing.com.au
      </li>
    </ul>

    <div class="back-wordmark">KT Crewing</div>

    <div class="company-details">
      <p class="acn"><span class="acn-label">ACN:</span> 718 235 946</p>
      <p class="slogan">Onsite Auto Electrician<br>Labour Hire</p>
    </div>

    <div class="person">
      <p class="person-name">Marcus Mick</p>
      <p class="person-title">Managing Director</p>
    </div>
  </section>
</main>
</body>
</html>
```